continuing medical education travel company. luxury, professional, quality service

PLEASE USE THE REVISED LOGO FOR ALL CARD DESIGNS, NO SNAKE HEAD

Target Market(s)

physicians

Industry/Entity Type

Travel Industry

Contact Information for Business Card

luxury quality, spot uv, foil, rounded corners

Colors
0255a3
3176b5
cfdeed
aaaaaa
5c5c5c

Requirements
Must have
• navy, platinum, possible holographic

```html
<!DOCTYPE html>
<html lang="en">
<head>
<meta charset="utf-8">
<title>Meridian Travel – Business Cards</title>
<link rel="stylesheet" href="https://fonts.googleapis.com/css2?family=Open+Sans:wght@400;700&display=swap">
<style>
  :root {
    --navy: #2e3192;
    --grey: #7a7a7a;
    --grey-light: #8c8c8c;
    --text-grey: #5c5c5c;
    --card-dark: #2b2b2b;
    --platinum: #e4e4ea;
    --paper: #ffffff;
    --backdrop: #ece9e4;
  }
  * { box-sizing: border-box; margin: 0; padding: 0; }
  html, body {
    width: 1200px; height: 900px; overflow: hidden;
    background: var(--backdrop);
    font-family: "Open Sans", Arial, sans-serif;
  }
  .canvas { position: relative; width: 1200px; height: 900px; }
  .card {
    position: absolute; width: 580px; height: 331px;
    border-radius: 10px; overflow: hidden;
    box-shadow: 0 10px 28px rgba(0,0,0,0.18);
  }
  .card-back {
    left: 560px; top: 80px;
    background: var(--card-dark);
    display: flex; align-items: center; justify-content: center;
  }
  .card-front { left: 60px; top: 480px; background: var(--paper); }
  .wordmark {
    display: flex; align-items: center; gap: 12px;
    font-weight: 700; font-size: 38px; letter-spacing: 1px; line-height: 1;
  }
  .wordmark .dot { width: 14px; height: 14px; border-radius: 50%; }
  .card-back .wordmark { color: var(--platinum); }
  .card-back .wordmark .dot { background: var(--platinum); }
  .card-front .wordmark {
    position: absolute; right: 40px; top: 140px;
    color: var(--navy); font-size: 34px;
  }
  .card-front .wordmark .dot { background: var(--navy); }
  .card-art { position: absolute; inset: 0; }
  .holder { position: absolute; left: 70px; top: 18px; }
  .holder-name { color: var(--navy); font-weight: 700; font-size: 19px; }
  .holder-title { color: var(--grey); font-size: 13px; margin-top: -2px; }
  .address {
    position: absolute; left: 42px; top: 100px;
    color: var(--text-grey); font-size: 13px; line-height: 1.4;
  }
  .contacts {
    position: absolute; left: 20px; top: 150px;
    list-style: none; color: var(--text-grey); font-size: 13.5px; line-height: 1.45;
  }
  .contacts li { display: flex; align-items: center; gap: 8px; }
  .contacts svg { width: 12px; height: 12px; fill: var(--navy); flex: none; }
</style>
</head>
<body>
<main class="canvas">

  <section class="card card-back" aria-label="Card back">
    <div class="wordmark"><span class="dot"></span>Meridian Travel</div>
  </section>

  <section class="card card-front" aria-label="Card front">
    <svg class="card-art" viewBox="0 0 580 331" aria-hidden="true">
      <polygon points="0,0 40,0 14,38 0,38" fill="var(--navy)"/>
      <polygon points="46,0 62,0 62,38 20,38" fill="var(--grey-light)"/>
      <polygon points="0,232 290,303 282,331 0,331" fill="var(--navy)"/>
      <polygon points="300,292 580,292 580,331 290,331" fill="var(--grey)"/>
    </svg>

    <div class="holder">
      <p class="holder-name">Laura Bennett</p>
      <p class="holder-title">Principal</p>
    </div>

    <p class="address">18 Harbour Lane, Lakeview<br>QC H1A 2B3</p>

    <ul class="contacts">
      <li><svg viewBox="0 0 12 12"><path d="M2.5 0.5l2 2.2-1 1.3c.7 1.6 1.9 2.8 3.5 3.5l1.3-1 2.2 2-1.2 2.3C4.8 10.5 1.5 7.2 0.3 2z"/></svg>555.010.2468</li>
      <li><svg viewBox="0 0 12 12"><path d="M0 2h12v8H0z M0.8 2.6l5.2 4 5.2-4" stroke="#fff" stroke-width="0.9"/></svg>lbennett@meridiantravel.com</li>
      <li><svg viewBox="0 0 12 12"><circle cx="6" cy="6" r="5.5"/></svg>meridiantravel.com</li>
    </ul>

    <div class="wordmark"><span class="dot"></span>Meridian Travel</div>
  </section>

</main>
</body>
</html>
```